Fitness Camp Flyer Design

We need a modern, fresh, inspiring flyer design for our new fitness retreat compant called " Tidewell Vigour Retreats". We run Fitness and weight loss retreats for customers who need to get rapid, fast and effective results in short spaces of time. Our Fitness camps are residential but we do also offer a day stay program for locals. We would like to see a design that mirrors our website in terms of colours and message www.tidewellvigourretreats.com.au . The final design should comminicate fast fitness and weight loss results in the best locations and with the best fitness retreat company in Australia
Updates

A 5 SIZE FLYER. I ALSO HAVE AN IMAGE I NEED ON THE FLYER BUT I CANT DOWNLOAD TO PIXEL BAZAAR CAN YOU SEND EMAIL SO I CAN GET IT TO YOU. THANKS

Target Market(s)

mainly females but males also, 18 - 45, fitness and weight loss motivated, in need of a fitness break

Industry/Entity Type

Residential

Requirements
Must have
• Must have images for happy fitness groups
Must have images of our Sydney Vigour Retreat
Must be moden and energetic in design
Must be double sided
Must include text " Sydney Northern Beaches Fitness Retreat"
Must include text " Get Fit, Lose Weight and Tone Your Body Fast!
Must include a testomonial " I lost 8 kilos with my stay at Tidewell and now feel great" Joan - Sydney
Must include web address www.tidewellvigourretreats.com.au
Must include contact number 1300 572 386
Must include email info@tidewellvigourretreats.com.au

Must have " Day Stay Program For Locals "

Must have in bullet points
4 star Villas
Stunning coastal and lakeside location
Sydney Northern Beaches
1st class health club access
Outdoor swimming pools
In Room Massage
Direct beach access
Daily fitness program
Healthy meals
From only $995 per week

Also must include: Variety of Exercise Classes including
Beach Boot Camp
Circuit Training
Burn Surge
Boxing Classes
Circuit Training
Interval Training
Gym Training
Outdoor Fitness Treks
Yoga
Plus many more!

base design around the colours and feel of www.tidewellvigourretreats.com.au
Nice to have
• Keep it fresh, modern and inspirational

```html
<!DOCTYPE html>
<html lang="en">
<head>
<meta charset="utf-8">
<title>Tidewell Vigour Retreats – Day Stay Program</title>
<link rel="stylesheet" href="https://fonts.googleapis.com/css2?family=Montserrat:wght@600;700&family=Questrial&display=swap">
<style>
  :root {
    --orange: #ee7d1a;
    --green: #7cc021;
    --green-band: #82c226;
    --white: #ffffff;
    --heading-font: "Montserrat", sans-serif;
    --body-font: "Questrial", sans-serif;
  }
  * { margin: 0; padding: 0; box-sizing: border-box; }
  html, body { width: 900px; height: 1200px; overflow: hidden; background: var(--white); }
  .flyer { position: relative; width: 900px; height: 1200px; background: var(--white); overflow: hidden; }

  .heading {
    position: absolute; left: 97px;
    font-family: var(--heading-font); font-weight: 600;
    font-size: 39px; line-height: 52px; letter-spacing: 2.4px;
    color: var(--orange);
  }
  .heading--day-stay { top: 17px; }
  .heading--classes { top: 467px; }

  .feature-list {
    position: absolute; left: 100px; list-style: none;
    font-family: var(--body-font); font-size: 26px; line-height: 39.4px;
    letter-spacing: 1.3px; color: var(--green);
  }
  .feature-list--amenities { top: 72px; }
  .feature-list--classes { top: 572px; }

  .waves { position: absolute; left: 0; top: 0; width: 900px; height: 1200px; }

  .class-photo {
    position: absolute; left: 603px; top: 688px; width: 297px; height: 325px;
    background: var(--green-band); padding: 8px 0 0 9px;
  }
  .class-photo__fill {
    width: 100%; height: 100%;
    background: linear-gradient(180deg, #9fb9c6 0%, #5f8a78 25%, #4c7a5f 48%, #8d8fa2 62%, #e9b47a 72%, #c99d83 82%, #b9a99c 100%);
  }

  .brand {
    position: absolute; right: 16px; top: 1122px;
    display: flex; align-items: center; gap: 10px;
    font-family: var(--heading-font); font-weight: 700; font-size: 30px;
    color: var(--orange); letter-spacing: -0.5px;
  }
  .brand__dot { width: 40px; height: 40px; border-radius: 50%; background: var(--orange); }
</style>
</head>
<body>
<main class="flyer">
  <svg class="waves" viewBox="0 0 900 1200" aria-hidden="true">
    <path fill="#82c226" d="M0,943 C200,952 340,1015 620,1008 L900,1003 L900,1052 C600,1040 300,1030 0,1030 Z"/>
    <path fill="#ee7d1a" d="M0,1030 C300,1030 600,1040 900,1052 L900,1106 C620,1082 320,1070 0,1078 Z"/>
  </svg>

  <h1 class="heading heading--day-stay">Day Stay Program For Locals</h1>
  <ul class="feature-list feature-list--amenities">
    <li>4 star Villas</li>
    <li>Stunning coastal and lakeside location</li>
    <li>Sydney Northern Beaches</li>
    <li>1st class health club access</li>
    <li>Outdoor swimming pools</li>
    <li>In Room Massage</li>
    <li>Direct beach access</li>
    <li>Daily fitness program</li>
    <li>Healthy meal</li>
    <li>From only $995 per week</li>
  </ul>

  <h2 class="heading heading--classes">Variety of Exercise Classes<br>including</h2>
  <ul class="feature-list feature-list--classes">
    <li>Beach Boot Camp</li>
    <li>Circuit Training</li>
    <li>Burn Surge</li>
    <li>Boxing Classes</li>
    <li>Circuit Training</li>
    <li>Interval Training</li>
    <li>Gym Training</li>
    <li>Outdoor Fitness Treks</li>
    <li>Yoga</li>
    <li>Plus many more!</li>
  </ul>

  <figure class="class-photo">
    <div class="class-photo__fill" role="img" aria-label="Photo collage: a group boxing class on an outdoor court, and a sunrise fitness session on the beach with exercise balls"></div>
  </figure>

  <div class="brand">
    <span class="brand__dot"></span>
    <span class="brand__name">Tidewell Vigour Retreats</span>
  </div>
</main>
</body>
</html>
```